Business Card Design

Please visit www.RobHartwell.com to acquire information for business card.

Back Side of Card:
a lifetime of experience working for you.

With over 25 years in the construction industry, well over a decade as a licensed Subcontractor / General Contractor and nearly 10 years as a licensed Realtor, I have excelled and cultivated a working knowledge of how all the pieces fit together.

Here is a link to folder.
https://files.examplestore.net/folderview?id=7Kq2XwPmR4tLvN9sBz8yHc3DfGaJ&usp=sharing

Industry/Entity Type

Construction

Contact Information for Business Card

Company: Rob Hartwell, LLC.
Address: 31872 W. Cedar Hollow Blvd. Suite 207-384
Name: Rob Hartwell
Phone: (623) 587-2914
Web: www.RobHartwell.com
Type of services offered: Architectural Design, 3D Models, Renderings & Animation - Construction Documents - Project Managment.

```html
<!DOCTYPE html>
<html lang="en">
<head>
<meta charset="utf-8">
<title>Rob Hartwell, LLC. – Business Card</title>
<link href="https://fonts.googleapis.com/css2?family=Didact+Gothic&family=Questrial&display=swap" rel="stylesheet">
<style>
  :root {
    --backdrop: #3d4547;
    --card-blue: #3082ff;
    --front-text: #5aa6f2;
    --card-dark: #1c1f20;
    --ink: #111314;
    --muted: #6d7275;
    --icon-blue: #3a86f5;
  }
  * { margin: 0; padding: 0; box-sizing: border-box; }
  html, body { width: 1200px; height: 741px; overflow: hidden; }
  body {
    background: var(--backdrop);
    position: relative;
    font-family: "Didact Gothic", "Questrial", sans-serif;
  }
  .card {
    position: absolute;
    left: 399px;
    width: 409px;
    height: 237px;
    overflow: hidden;
  }
  .card-front {
    top: 88px;
    background: var(--card-blue);
    display: flex;
    align-items: center;
    justify-content: center;
  }
  .company-name {
    font-family: "Questrial", sans-serif;
    font-size: 35px;
    color: var(--front-text);
    letter-spacing: 0.5px;
  }
  .card-back {
    top: 413px;
    background: var(--card-dark);
  }
  .name-band {
    position: absolute;
    left: 0; right: 0;
    top: 68px;
    height: 97px;
    background: var(--card-blue);
  }
  .first-name, .last-name {
    position: absolute;
    font-size: 28px;
    line-height: 1;
    letter-spacing: 1px;
  }
  .first-name { left: 29px; top: 42px; color: var(--card-blue); }
  .last-name { left: 89px; top: 64px; color: var(--ink); }
  .services {
    position: absolute;
    left: 31px;
    top: 126px;
    font-size: 12px;
    line-height: 18px;
    color: var(--ink);
    white-space: nowrap;
  }
  .services span { display: block; }
  .services .indent { padding-left: 21px; }
  .contact {
    position: absolute;
    display: flex;
    align-items: center;
    gap: 9px;
    font-size: 12px;
    color: var(--muted);
    letter-spacing: 0.6px;
    white-space: nowrap;
  }
  .contact svg { width: 11px; height: 11px; fill: var(--icon-blue); flex: none; }
  .contact-phone { left: 33px; top: 195px; }
  .contact-web { left: 206px; top: 195px; }
  .contact-address { left: 33px; top: 217px; }
  .contact-address .suite { margin-left: 10px; }
</style>
</head>
<body>
  <section class="card card-front" aria-label="Card front">
    <h1 class="company-name">Rob Hartwell, LLC.</h1>
  </section>

  <section class="card card-back" aria-label="Card back">
    <div class="name-band"></div>
    <div class="first-name">ROB</div>
    <div class="last-name">HARTWELL</div>
    <p class="services">
      <span>Architectural Design, 3D Models, Renderings &amp; Animation</span>
      <span class="indent">Construction Documents - Project Managment.</span>
    </p>
    <div class="contact contact-phone">
      <svg viewBox="0 0 24 24" aria-hidden="true"><path d="M6.6 10.8a15.2 15.2 0 0 0 6.6 6.6l2.2-2.2a1 1 0 0 1 1-.25 11.4 11.4 0 0 0 3.6.57 1 1 0 0 1 1 1V20a1 1 0 0 1-1 1A17 17 0 0 1 3 4a1 1 0 0 1 1-1h3.5a1 1 0 0 1 1 1c0 1.25.2 2.45.57 3.6a1 1 0 0 1-.25 1z"/></svg>
      <span>(623) 587-2914</span>
    </div>
    <div class="contact contact-web">
      <svg viewBox="0 0 24 24" aria-hidden="true"><circle cx="12" cy="12" r="10"/><path d="M2 12h20M12 2c3 3 3 17 0 20M12 2c-3 3-3 17 0 20" stroke="#1c1f20" stroke-width="1.6" fill="none"/></svg>
      <span>www.robhartwell.com</span>
    </div>
    <div class="contact contact-address">
      <svg viewBox="0 0 24 24" aria-hidden="true"><path d="M12 2a7 7 0 0 0-7 7c0 5.2 7 13 7 13s7-7.8 7-13a7 7 0 0 0-7-7zm0 9.5A2.5 2.5 0 1 1 12 6.5a2.5 2.5 0 0 1 0 5z"/></svg>
      <span>31872 W. Cedar Hollow Blvd.<span class="suite">Suite 207-384</span></span>
    </div>
  </section>
</body>
</html>
```